KESTRIDGE PAINTING

We are a painting company. We paint residential, commercial and strata jobs. I need the website to be very sharp, neat and elegant. I've attached our logo. the Logo needs to be embossed as a gold color and the background like a Matt black. I need these tabs:

• HOME • ABOUT US • SERVICES • TESTIMONIALS • SHOWCASE • CONTACT US

Be creative and innovative in your style.
take this as an example to just get the gist of what I'm expecting. If you can better it then the job is yours!

http://marlowvinepainting.com.au/contact.html

I look forward to seeing your artwork :)

#These are the links to my logo in PSD format.

https://www.filevaultic.com/s/qwpzrtk4n7hd2aa/Kestridge%20Painting%20Luxury%20Gold.rar

https://www.filevaultic.com/sh/rkvbnxq2p5yhw7/QaLm8-vbSx

• Making the Logo embossed like the artworks i have attached is definitely a necessity.

Can you let me know if this is possible to apply to the website.

thank you

```html
<!DOCTYPE html>
<html lang="en">
<head>
<meta charset="utf-8">
<title>Kestridge Painting</title>
<link rel="stylesheet" href="https://fonts.googleapis.com/css2?family=Source+Sans+3:ital,wght@0,400;0,600;0,700;1,400&display=swap">
<style>
:root{
  --ink:#1e222a;
  --gold:#e3b34a;
  --gold-deep:#d19e14;
  --gold-light:#f3d89c;
  --grey-dark:#4a4e55;
  --grey-mid:#6f7379;
  --grey-light:#9a9da2;
  --rule:#4a4f57;
  --white:#ffffff;
  --footer:#464a50;
}
*{margin:0;padding:0;box-sizing:border-box}
html,body{width:1157px;height:1200px;overflow:hidden;background:var(--ink)}
body{position:relative;font-family:"Source Sans 3",sans-serif;color:var(--white)}
.top-bar{position:absolute;left:0;top:0;width:1157px;height:89px;background:var(--ink);border-bottom:1px solid var(--gold)}
.phone-top{position:absolute;right:160px;top:10px;color:var(--gold);font-size:22px;padding-bottom:4px;border-bottom:2px solid var(--gold);display:flex;align-items:center;gap:8px}
.main-nav{position:absolute;right:160px;top:61px;display:flex;gap:30px;font-weight:600;font-size:14.5px;letter-spacing:.6px}
.main-nav a{color:var(--white);text-decoration:none}
.main-nav a.active{color:var(--gold)}
.hero{position:absolute;left:0;top:89px;width:1157px;height:436px;background:linear-gradient(180deg,#5d4537 0%,#7a5a45 35%,#8e6b52 60%,#b99c88 85%,#a88d7a 100%)}
.brand-strip{position:absolute;left:270px;top:89px;width:487px;height:39px;background:linear-gradient(90deg,#e9c978,#f2d98f 50%,#e3b84e);display:flex;align-items:center;padding-left:13px}
.brand-name{color:var(--ink);font-weight:700;font-size:22px;letter-spacing:1.2px}
.brand-sep{width:1px;height:18px;background:#b8902a;margin:0 14px}
.brand-tag{color:var(--ink);font-style:italic;font-size:18px}
.logo-disc{position:absolute;left:164px;top:24px;width:107px;height:107px;border-radius:50%;background:var(--ink);border:3px solid var(--gold)}
.slider-dots{position:absolute;right:160px;top:119px;display:flex;gap:8px}
.slider-dots span{width:9px;height:9px;background:#3a3d42}
.slider-dots span.on{background:var(--gold)}
.caption-accent-a{position:absolute;left:160px;top:324px;width:53px;height:53px;background:var(--gold)}
.caption-accent-b{position:absolute;left:641px;top:378px;width:160px;height:98px;background:var(--gold)}
.caption-accent-c{position:absolute;left:749px;top:333px;width:34px;height:6px;background:#9b9ea3}
.caption{position:absolute;left:169px;top:333px;width:614px;height:133px;background:var(--ink);padding:16px 34px;font-size:45px;line-height:48px;font-weight:400}
.color-band{position:absolute;left:0;display:flex;height:9px}
.color-band span{height:100%}
.welcome{position:absolute;left:159px;top:568px;width:533px}
.welcome h1{color:var(--gold);font-size:42px;font-weight:700;margin-bottom:24px}
.welcome p{font-size:14.5px;line-height:26.7px;margin-bottom:26.7px}
.more-link{position:absolute;left:574px;top:1046px;color:var(--gold);font-weight:700;font-size:17px;padding-bottom:3px;border-bottom:2px dotted var(--gold)}
.sidebar{position:absolute;left:756px;top:582px;width:241px}
.sidebar h2{color:var(--gold);font-size:27px;font-weight:700;margin-bottom:10px}
.contact-list{border-top:1px solid var(--rule)}
.contact-row{display:flex;border-bottom:1px solid var(--rule)}
.contact-row:last-child{border-bottom:none}
.contact-icon{width:32px;flex:none;border-right:1px solid var(--rule);display:flex;justify-content:center;padding-top:12px}
.contact-text{padding:9px 0 10px 14px;font-size:14px;line-height:18px}
.contact-text.big{font-size:21px;font-weight:600;line-height:26px}
.follow{margin-top:48px}
.social{display:flex;gap:16px;padding:14px 0 20px;border-bottom:1px solid var(--rule)}
.social span{width:29px;height:29px;border-radius:50%;background:#9c9fa4}
.social span.first{background:#3b5a98}
.footer{position:absolute;left:0;top:1137px;width:1157px;height:63px;background:var(--footer);padding:29px 0 0 161px;font-size:12.5px}
</style>
</head>
<body>
<header class="top-bar">
  <div class="phone-top">
    <svg width="18" height="18" viewBox="0 0 24 24"><path fill="#e3b34a" d="M6.6 10.8c1.4 2.8 3.8 5.1 6.6 6.6l2.2-2.2c.3-.3.7-.4 1-.2 1.1.4 2.3.6 3.6.6.6 0 1 .4 1 1V20c0 .6-.4 1-1 1C10.6 21 3 13.4 3 4c0-.6.4-1 1-1h3.5c.6 0 1 .4 1 1 0 1.3.2 2.5.6 3.6.1.3 0 .7-.2 1z"/></svg>
    1300 47 19 52
  </div>
  <nav class="main-nav">
    <a class="active" href="#">HOME</a><a href="#">ABOUT US</a><a href="#">SERVICES</a><a href="#">TESTIMONIALS</a><a href="#">SHOWCASE</a><a href="#">CONTACT US</a>
  </nav>
</header>
<div class="hero" role="img" aria-label="Photo of a living room with a brown and cream leather sofa"></div>
<div class="brand-strip"><span class="brand-name">KESTRIDGE PAINTING</span><span class="brand-sep"></span><span class="brand-tag">Crafted Colour, Every Day!</span></div>
<div class="logo-disc"></div>
<div class="slider-dots"><span></span><span></span><span></span><span class="on"></span></div>
<div class="caption-accent-a"></div>
<div class="caption-accent-b"></div>
<div class="caption-accent-c"></div>
<div class="caption">We paint residential,<br>commercial and strata jobs</div>
<div class="color-band" style="top:525px">
  <span style="width:277px;background:var(--ink)"></span><span style="width:79px;background:var(--grey-dark)"></span><span style="width:88px;background:var(--grey-mid)"></span><span style="width:136px;background:var(--grey-light)"></span><span style="width:116px;background:var(--gold-deep)"></span><span style="width:79px;background:#e0ae3c"></span><span style="width:87px;background:#f0c878"></span><span style="width:295px;background:var(--gold-light)"></span>
</div>
<main class="welcome">
  <h1>Welcome!</h1>
  <p>Lorem ipsum dolor sit amet, consectetur adipiscing elit. Quantum Aristoxeni ingenium consumptum videmus in musicis? Nihil enim hoc differt. Re mihi non aeque satisfacit, et quidem locis pluribus. At iste non dolendi status non vocatur voluptas. Quamquam haec quidem praeposita recte et reiecta dicere licebit.</p>
  <p>Duo Reges: constructio interrete. Inde sermone vario sex illa a Dipylo stadia confecimus. Ad quorum et cognitionem et usum iam corroborati natura ipsa praeeunte deducimur. Idem iste, inquam, de voluptate quid sentit? Septem autem illi non suo, sed populorum suffragio omnium nominati sunt. Quamquam haec quidem praeposita recte et reiecta dicere licebit. Atqui eorum nihil est eius generis, ut sit in fine atque extrerno bonorum.</p>
  <p>Atqui reperies, inquit, in hoc quidem pertinacem; Sin autem est in ea, quod quidam volunt, nihil impedit hanc nostram comprehensionem summi boni. Urgent tamen et nihil remittunt. Avaritiamne minuis.</p>
</main>
<a class="more-link">MORE ABOUT US</a>
<aside class="sidebar">
  <h2>Contact us</h2>
  <div class="contact-list">
    <div class="contact-row">
      <div class="contact-icon"><svg width="20" height="22" viewBox="0 0 20 22"><rect x="9" y="1" width="2" height="20" fill="#9a9da2"/><path d="M2 3h14l3 2.5-3 2.5H2z" fill="#9a9da2"/><path d="M18 9H5l-3 2.5L5 14h13z" fill="#9a9da2"/></svg></div>
      <div class="contact-text">Lorem ipsum dolor sit amet consectetur adipiscing elit Quantum Aristoxeni ingenium consumptum.</div>
    </div>
    <div class="contact-row">
      <div class="contact-icon"><svg width="18" height="18" viewBox="0 0 24 24"><path fill="#9a9da2" d="M6.6 10.8c1.4 2.8 3.8 5.1 6.6 6.6l2.2-2.2c.3-.3.7-.4 1-.2 1.1.4 2.3.6 3.6.6.6 0 1 .4 1 1V20c0 .6-.4 1-1 1C10.6 21 3 13.4 3 4c0-.6.4-1 1-1h3.5c.6 0 1 .4 1 1 0 1.3.2 2.5.6 3.6.1.3 0 .7-.2 1z"/></svg></div>
      <div class="contact-text big">1300 47 19 52</div>
    </div>
    <div class="contact-row">
      <div class="contact-icon"><svg width="20" height="14" viewBox="0 0 20 14"><rect x=".5" y=".5" width="19" height="13" fill="none" stroke="#9a9da2"/><path d="M.5.5l9.5 7 9.5-7M.5 13.5l7-6M19.5 13.5l-7-6" fill="none" stroke="#9a9da2"/></svg></div>
      <div class="contact-text">mail@kestridgepainting.com.au</div>
    </div>
  </div>
  <div class="follow">
    <h2>Follow us</h2>
    <div class="social"><span class="first"></span><span></span><span></span><span></span></div>
  </div>
</aside>
<div class="color-band" style="top:1128px">
  <span style="width:295px;background:var(--gold-light)"></span><span style="width:87px;background:#f0c878"></span><span style="width:79px;background:#e0ae3c"></span><span style="width:117px;background:var(--gold-deep)"></span><span style="width:136px;background:var(--grey-light)"></span><span style="width:87px;background:var(--grey-mid)"></span><span style="width:79px;background:var(--grey-dark)"></span>
</div>
<footer class="footer">Copyright @ 2013 Kestridge Painting. All rights reserved.</footer>
</body>
</html>
```